Business card for law firm

Need business card for new law firm. Think confident, authoritative, conservative, but not stuffy or old-fashioned.

Contact Information for Business Card

Content for card - logo (uploaded), plus the following:

Paul Wexbury (larger font)
Managing Partner (larger font, but not as large as name)
Level 9, 41 Tansy Lane
Sydney NSW 2000
Main Tel 02 7346 2190
Direct Tel 02 6273 4415
Email paul@qvlegal.com.au
www.qvlegal.com.au

Letterhead design should include logo plus:
Level 9, 41 Tansy Lane
Sydney NSW 2000
Tel 02 6273 4415
www.qvlegal.com.au

```html
<!DOCTYPE html>
<html lang="en">
<head>
<meta charset="utf-8">
<title>Quaverly Legal – Business Card</title>
<link href="https://fonts.googleapis.com/css2?family=Cinzel:wght@400;500&family=Lato:wght@400;700&display=swap" rel="stylesheet">
<style>
  :root {
    --navy: #1f2470;
    --navy-deep: #161a57;
    --paper: #f7f7f5;
    --ink: #1a1a1a;
    --ghost: #dcdcdc;
    --stage: #2a2a2a;
    --white: #ffffff;
  }
  * { box-sizing: border-box; margin: 0; padding: 0; }
  html, body { width: 1200px; height: 900px; overflow: hidden; }
  body {
    background: var(--stage);
    position: relative;
    font-family: "Lato", sans-serif;
  }
  .card {
    position: absolute;
    left: 320px;
    width: 560px;
    height: 320px;
    border-radius: 26px;
    overflow: hidden;
  }
  .card--front {
    top: 100px;
    background: radial-gradient(ellipse at 45% 35%, var(--navy) 0%, var(--navy-deep) 100%);
    color: var(--white);
  }
  .card--back {
    top: 480px;
    background: var(--paper);
    color: var(--ink);
  }

  /* front */
  .brand {
    position: absolute;
    top: 72px; left: 0; right: 0;
    display: flex; flex-direction: column; align-items: center;
  }
  .brand__mark {
    width: 64px; height: 64px;
    background: var(--white);
  }
  .brand__name {
    margin-top: 20px;
    font-family: "Cinzel", serif;
    font-weight: 400;
    font-size: 34px;
    letter-spacing: 4px;
    line-height: 1;
    color: var(--white);
  }
  .front__url {
    position: absolute;
    bottom: 46px; left: 0; right: 0;
    text-align: center;
    font-size: 14px;
    letter-spacing: 3px;
    color: var(--white);
  }

  /* back */
  .ghost-name {
    position: absolute;
    left: 10px; top: 290px;
    transform: rotate(-90deg);
    transform-origin: left top;
    white-space: nowrap;
    color: var(--ghost);
  }
  .ghost-name__main {
    display: block;
    font-family: "Cinzel", serif;
    font-size: 34px;
    line-height: 36px;
    letter-spacing: 3px;
  }
  .ghost-name__sub {
    display: block;
    font-family: "Cinzel", serif;
    font-size: 12px;
    line-height: 14px;
    letter-spacing: 9px;
    padding-left: 40px;
  }
  .back-brand {
    position: absolute;
    top: 38px; right: 44px;
    display: flex; flex-direction: column; align-items: center;
  }
  .back-brand__mark { width: 72px; height: 72px; background: var(--navy); }
  .back-brand__name {
    margin-top: 8px;
    font-family: "Cinzel", serif;
    font-size: 12px;
    letter-spacing: 2px;
    color: var(--navy);
  }
  .person { position: absolute; left: 78px; top: 74px; }
  .person__name {
    font-family: "Cinzel", serif;
    font-size: 22px;
    letter-spacing: 0.5px;
    color: var(--ink);
  }
  .person__role {
    font-size: 14px;
    font-weight: 700;
    color: var(--navy);
    margin-top: 2px;
  }
  .contact {
    position: absolute;
    left: 78px; top: 168px;
    list-style: none;
    font-size: 13px;
    line-height: 20px;
    color: var(--ink);
  }
  .contact li { display: flex; align-items: flex-start; gap: 10px; }
  .contact svg { width: 12px; height: 12px; margin-top: 4px; fill: var(--navy); flex: none; }
  .rule {
    position: absolute;
    left: 300px; right: 0; top: 206px;
    height: 2px; background: var(--navy);
  }
  .back__url {
    position: absolute;
    right: 40px; top: 180px;
    font-size: 13px;
    color: var(--navy);
  }
</style>
</head>
<body>

<section class="card card--front" aria-label="Card front">
  <div class="brand">
    <div class="brand__mark"></div>
    <div class="brand__name">QUAVERLY LEGAL</div>
  </div>
  <p class="front__url">www.qvlegal.com.au</p>
</section>

<section class="card card--back" aria-label="Card back">
  <div class="ghost-name" aria-hidden="true">
    <span class="ghost-name__main">QUAVERLY</span>
    <span class="ghost-name__sub">LEGAL</span>
  </div>

  <div class="back-brand">
    <div class="back-brand__mark"></div>
    <div class="back-brand__name">QUAVERLY LEGAL</div>
  </div>

  <div class="person">
    <h1 class="person__name">PAUL WEXBURY</h1>
    <p class="person__role">MANAGING PARTNER</p>
  </div>

  <ul class="contact">
    <li>
      <svg viewBox="0 0 12 12"><path d="M6 0a4 4 0 0 0-4 4c0 3 4 8 4 8s4-5 4-8a4 4 0 0 0-4-4zm0 5.6A1.6 1.6 0 1 1 6 2.4a1.6 1.6 0 0 1 0 3.2z"/></svg>
      <span>Level 9, 41 Tansy Lane<br>Sydney NSW 2000</span>
    </li>
    <li>
      <svg viewBox="0 0 12 12"><path d="M1 4c0-2 2-3 5-3s5 1 5 3v1H8.5V4h-5v1H1zM2.5 6h7l1 5h-9z"/></svg>
      <span>02 7346 2190 (Main)</span>
    </li>
    <li>
      <svg viewBox="0 0 12 12"><path d="M1 4c0-2 2-3 5-3s5 1 5 3v1H8.5V4h-5v1H1zM2.5 6h7l1 5h-9z"/></svg>
      <span>02 6273 4415 (Direct)</span>
    </li>
    <li>
      <svg viewBox="0 0 12 12"><path d="M0 2h12v1L6 7 0 3zm0 2.4 6 4 6-4V10H0z"/></svg>
      <span>paul@qvlegal.com.au</span>
    </li>
  </ul>

  <p class="back__url">www.qvlegal.com.au</p>
  <div class="rule"></div>
</section>

</body>
</html>
```